Business Card Design & logo

Residential building renovation and maintenance work.
All carpentry and joinery needs.
Laying solid timber and floating floors.
Kitchen and bathroom makeovers and modifications.
Interior fitouts,
small job specialist. tiling, plastering, painting,

I would like a silver background. With the use of different shades of grey, rustic orange, black and white.
I do not want pictures of hammers, chisels etc. I am looking for a logo to be incorporated into the card.

Carpentry

Contact Information for Business Card

BTQ Renovations and Maintenance
Lewis Tolbane
0471852036
info@btqfixes.com.au
btqfixes.com.au

```html
<!DOCTYPE html>
<html lang="en">
<head>
<meta charset="utf-8">
<title>BTQ Renovations and Maintenance – Business Cards</title>
<link href="https://fonts.googleapis.com/css2?family=Open+Sans:ital,wght@0,400;0,600;0,700;1,400&display=swap" rel="stylesheet">
<style>
  :root {
    --backdrop: #d9d9d9;
    --card: #080808;
    --ink: #f2f2f2;
    --ink-soft: #cfcfcf;
    --rule: #e6e6e6;
    --shadow: rgba(0,0,0,0.35);
  }
  * { margin: 0; padding: 0; box-sizing: border-box; }
  html, body {
    width: 1200px; height: 885px; overflow: hidden;
    background: var(--backdrop);
    font-family: "Open Sans", Arial, sans-serif;
    color: var(--ink);
  }
  .stage {
    width: 1200px; height: 885px;
    display: flex; flex-direction: column;
    align-items: center; justify-content: center; gap: 56px;
  }
  .card {
    width: 620px; height: 354px;
    background: var(--card);
    border-radius: 3px;
    box-shadow: 0 10px 28px var(--shadow);
    position: relative;
    overflow: hidden;
  }

  /* Brand lockup */
  .brand { display: flex; flex-direction: column; align-items: flex-start; }
  .brand-row { display: flex; align-items: flex-end; gap: 10px; }
  .brand-mark {
    width: 22px; height: 22px; background: var(--ink);
    margin-bottom: 23px;
    flex: none;
  }
  .brand-name {
    display: block;
    font-weight: 700; font-size: 86px; letter-spacing: -2px;
    line-height: 1.3; color: var(--ink);
  }
  .brand-tagline {
    display: block;
    font-weight: 600; font-size: 13.5px; line-height: 18px; color: var(--ink);
    margin-top: 2px; margin-left: 32px; letter-spacing: 0.1px;
    white-space: nowrap;
  }

  /* Front card */
  .card-front .brand { position: absolute; left: 42px; top: 46px; }
  .card-front .person {
    position: absolute; right: 46px; top: 112px;
    font-weight: 600; font-size: 24px; line-height: 1.2;
  }
  .card-front .divider {
    position: absolute; left: 42px; right: 46px; top: 196px;
    height: 2px; background: var(--rule);
  }
  .contact-list {
    position: absolute; left: 42px; bottom: 44px;
    list-style: none; display: flex; flex-direction: column; gap: 10px;
  }
  .contact-item {
    display: flex; align-items: center; gap: 14px;
    font-size: 20px; line-height: 1.3; color: var(--ink);
  }
  .contact-icon {
    width: 18px; height: 18px; background: var(--ink);
    border-radius: 2px; display: flex; align-items: center; justify-content: center;
    flex: none;
  }
  .website {
    position: absolute; right: 46px; bottom: 46px;
    font-size: 18px; line-height: 1.3; color: var(--ink-soft);
  }

  /* Back card */
  .services {
    position: absolute; left: 40px; top: 38px;
    list-style: none; display: flex; flex-direction: column; gap: 6px;
  }
  .service {
    font-style: italic; font-size: 17px; line-height: 1.4; color: var(--ink);
    display: flex; align-items: center; gap: 12px;
  }
  .service::before {
    content: ""; width: 8px; height: 4px; background: var(--ink); flex: none;
  }
  .card-back .brand { position: absolute; right: 40px; bottom: 34px; }
</style>
</head>
<body>
<main class="stage">

  <section class="card card-front" aria-label="Business card front">
    <div class="brand">
      <div class="brand-row">
        <span class="brand-mark"></span>
        <span class="brand-name">btq</span>
      </div>
      <span class="brand-tagline">Renovations And Maintenance</span>
    </div>
    <p class="person">Lewis Tolbane</p>
    <div class="divider"></div>
    <ul class="contact-list">
      <li class="contact-item">
        <span class="contact-icon">
          <svg width="12" height="12" viewBox="0 0 24 24" aria-hidden="true"><path fill="#080808" d="M6.6 10.8a15 15 0 0 0 6.6 6.6l2.2-2.2c.3-.3.7-.4 1-.2 1.1.4 2.3.6 3.6.6.6 0 1 .4 1 1V20c0 .6-.4 1-1 1A17 17 0 0 1 3 4c0-.6.4-1 1-1h3.5c.6 0 1 .4 1 1 0 1.3.2 2.5.6 3.6.1.3 0 .7-.2 1z"/></svg>
        </span>
        0471852036
      </li>
      <li class="contact-item">
        <span class="contact-icon">
          <svg width="12" height="12" viewBox="0 0 24 24" aria-hidden="true"><rect x="2" y="5" width="20" height="14" fill="none" stroke="#080808" stroke-width="2.5"/><path d="M2 5l10 8 10-8" fill="none" stroke="#080808" stroke-width="2.5"/></svg>
        </span>
        info@btqfixes.com.au
      </li>
    </ul>
    <p class="website">btqfixes.com.au</p>
  </section>

  <section class="card card-back" aria-label="Business card back">
    <ul class="services">
      <li class="service">All carpentry and joinery needs</li>
      <li class="service">Laying solid timber and floating floors</li>
      <li class="service">Kitchen and bathroom makeovers and modifications</li>
      <li class="service">Interior fitouts</li>
      <li class="service">small job specialist. tiling, plastering, painting</li>
    </ul>
    <div class="brand">
      <div class="brand-row">
        <span class="brand-mark"></span>
        <span class="brand-name">btq</span>
      </div>
      <span class="brand-tagline">Renovations And Maintenance</span>
    </div>
  </section>

</main>
</body>
</html>
```